Chauffeur Car Driver Needing a design with/without logo for business cards

I'm a chauffeur car driver in Melbourne Australia. I have an extensive list of personal customers and need to provide a professional business card to new customers.
My business name is 'RivaPlus'.
I offer a personalised service to customer who need a transport alternative to taxis. I don't want it to look too 'upmarket' as i don't want it to seem too expensive or only for special occasions. The majority of my clients are business professionals who use me for airport transfers.
I definitely don't want the card/logo to have an image of a car/road etc. I prefer something abstract. A 'pencil-line'-type font will grab my attention but not absolutely necessary. Not too 'digital' or 'ultra - modern' looking.
I need the card to display the following information
Riva Plus - main logo/text
Chauffeur Cars - sub text
Marco Devilles
0452 918 306
bookings@RivaPlus.example.au
I would like the focus to be on 'RivaPlus' with everything else smaller.
Look forward to seeing ideas!!!!
Target Market(s)
Business Corporate Professionals
Industry/Entity Type
Airport
Requirements
Nice to have
- Pencil line type font
Should not have
- Images of cars, road, tyres, steering wheel etc.

```html
<!DOCTYPE html>
<html lang="en">
<head>
<meta charset="utf-8">
<title>RivaPlus Chauffeur Cars – Business Card</title>
<link rel="stylesheet" href="https://fonts.googleapis.com/css2?family=Poppins:wght@400;500;600&display=swap">
<style>
  :root {
    --canvas-bg: #ececec;
    --card-bg: #ffffff;
    --brand-slate: #8b9ea8;
    --ink-grey: #555759;
    --accent-red: #e03526;
  }
  * { margin: 0; padding: 0; box-sizing: border-box; }
  html, body {
    width: 1200px;
    height: 800px;
    overflow: hidden;
    background: var(--canvas-bg);
    font-family: "Poppins", sans-serif;
  }
  .business-card {
    position: absolute;
    left: 150px;
    top: 125px;
    width: 900px;
    height: 550px;
    background: var(--card-bg);
    overflow: hidden;
  }
  .brand {
    position: absolute;
    left: 220px;
    top: 70px;
    width: 500px;
    text-align: right;
  }
  .brand-name {
    display: block;
    font-size: 104px;
    font-weight: 500;
    line-height: 1;
    letter-spacing: -1px;
    color: var(--brand-slate);
  }
  .brand-tagline {
    display: block;
    margin-top: 6px;
    font-size: 34px;
    font-weight: 500;
    line-height: 1;
    letter-spacing: 1px;
    color: var(--ink-grey);
  }
  .contact {
    position: absolute;
    left: 385px;
    top: 300px;
  }
  .contact-name {
    font-size: 40px;
    font-weight: 500;
    line-height: 1.1;
    color: var(--accent-red);
    margin-bottom: 10px;
  }
  .contact-line {
    font-size: 27px;
    font-weight: 600;
    line-height: 1.45;
    color: var(--ink-grey);
  }
  .contact-line .label { margin-right: 14px; }
  .accent-band {
    position: absolute;
    left: 0;
    bottom: 0;
    width: 100%;
    height: 88px;
    background: var(--accent-red);
  }
</style>
</head>
<body>
  <main class="business-card">
    <header class="brand">
      <span class="brand-name">RivaPlus</span>
      <span class="brand-tagline">chauffeur cars</span>
    </header>
    <section class="contact">
      <p class="contact-name">Marco Devilles</p>
      <p class="contact-line"><span class="label">Phone:</span>0452 918 306</p>
      <p class="contact-line">bookings@RivaPlus.example.au</p>
    </section>
    <div class="accent-band"></div>
  </main>
</body>
</html>
```